Powerpoint Template needed for new Digital Consultancy

We have recently had our logo designed through Brushvale and would now like to extend the brand look & feel through to having a powerpoint template created that we can use as a master template within which to create our client presentations.
Typical slides required and in terms of what we would need templating is:

- Stylised header and footer for main content slides
- intro/front page slide
- contents page slide
- standardised font type and sizes, heading types (including sizes) for Level 1, Level 2 and Level 3 headings
- use of text colour and any standards/styling around when to use bold, underline, italics etc
- table styling for when we want to use tables in the presentation
- standards and styles around using bullet and number lists
- stylising use of imagery that is dropped in e.g. do all images have a certain border style or drop-shadow etc.
- style and slide layout/format for how team profiles are handled
- style and slide layout/format for how case studies are handled
- closing, contact-us page

We can send over logo files and colour/font styles etc used for the logo soon.

Target Market(s)

B2B professional clients that are either medium to large corporations or potentially some government departments.

Industry/Entity Type

Digital

Font styles to use
Sans Serif

Colors
ec1f27
f37122
f78f20
faa54b
f68d4d
0255a3

Requirements
Must have
• Ideally as many templated pages/master slide types as outlined above in the brief to meet the requirements of what the powerpoint deck will be used for. Namely client presentations and pitches.
• Versions of the logo are attached to give an idea of the colour palette and clean, modern style we are looking for, plus the type of font we are using and like.
• We are looking for the slide design to be modern, minimalistic, clean and not overuse of colour. Preferably a white slide background so it's easy to then read slide content when we populate the slides with text which will be in black.
Nice to have
• Not expecting to see too much more than simple use of the logo and a slide header perhaps using some sort of line as a break and then a simple footer as well.
• Consider using Abode font.
Should not have
• Too much block colour or elements that draw away from what will go in the main content body of our slides when we use them.

```html
<!DOCTYPE html>
<html lang="en">
<head>
<meta charset="utf-8">
<title>Project title – Lumenloop</title>
<link rel="stylesheet" href="https://fonts.googleapis.com/css2?family=Arimo:wght@400;700&display=swap">
<style>
  :root {
    --slide-bg: #ffffff;
    --hero-deep: #050d1c;
    --hero-mid: #0a2a55;
    --hero-bright: #4fb6ff;
    --title-navy: #0d2a4c;
    --text-black: #111111;
  }
  html, body {
    margin: 0;
    padding: 0;
    width: 1200px;
    height: 900px;
    overflow: hidden;
    background: var(--slide-bg);
  }
  .slide {
    position: relative;
    width: 1200px;
    height: 900px;
    background: var(--slide-bg);
    font-family: "Arimo", Arial, sans-serif;
    overflow: hidden;
  }
  .hero-visual {
    position: absolute;
    left: 0;
    top: 0;
    width: 1200px;
    height: 645px;
    background:
      radial-gradient(circle at 930px 130px, var(--hero-bright) 0, rgba(79,182,255,0.35) 70px, transparent 190px),
      radial-gradient(circle at 380px 190px, rgba(30,127,216,0.55) 0, transparent 260px),
      radial-gradient(circle at 80px 540px, rgba(30,127,216,0.45) 0, transparent 220px),
      linear-gradient(120deg, var(--hero-mid) 0%, var(--hero-deep) 55%, #0c1f3d 100%);
  }
  .corner-cut {
    position: absolute;
    left: 0;
    top: 0;
  }
  .brand-name {
    position: absolute;
    right: 22px;
    top: 596px;
    margin: 0;
    font-size: 30px;
    font-weight: 700;
    color: var(--title-navy);
    line-height: 1;
  }
  .title-block {
    position: absolute;
    left: 30px;
    top: 680px;
  }
  .project-title {
    margin: 0;
    font-size: 47px;
    font-weight: 700;
    color: var(--title-navy);
    line-height: 1.15;
  }
  .project-subtitle {
    margin: 22px 0 0;
    font-size: 33px;
    font-weight: 400;
    color: var(--text-black);
    line-height: 1.2;
  }
</style>
</head>
<body>
  <main class="slide">
    <div class="hero-visual" role="img" aria-label="Photograph of a business person's hand touching glowing blue technical gear outlines"></div>
    <svg class="corner-cut" width="1200" height="900" viewBox="0 0 1200 900" aria-hidden="true">
      <polygon points="908,646 1200,483 1200,646" fill="var(--slide-bg)"/>
    </svg>
    <p class="brand-name">Lumenloop</p>
    <section class="title-block">
      <h1 class="project-title">Project title</h1>
      <p class="project-subtitle">Subtitle</p>
    </section>
  </main>
</body>
</html>
```